Bramwick Drywall Business Card

Looking to update the imagery, colors and logo to a more current design and to reflect their specialty of "High End" residential home construction

```html
<!DOCTYPE html>
<html lang="en">
<head>
<meta charset="utf-8">
<title>Bramwick Drywall Business Card</title>
<link href="https://fonts.googleapis.com/css2?family=Montserrat:wght@500;600;700;800&family=Great+Vibes&display=swap" rel="stylesheet">
<style>
  :root{
    --red:#e3202a;
    --black:#0d0d0d;
    --ink:#1a1a1a;
    --white:#ffffff;
    --stage:#e9e6e1;
    --room-light:#f3efe9;
    --room-warm:#e0d8cc;
    --room-floor:#b9ab98;
    --room-glass:#cfdbe3;
    --room-plant:#7f9270;
    --badge-blue:#c9d0ea;
    --badge-grey:#d6d6d6;
    --badge-teal:#c6dde4;
    --badge-edge:#9aa3b5;
  }
  *{margin:0;padding:0;box-sizing:border-box}
  html,body{width:900px;height:1200px;overflow:hidden}
  body{background:var(--stage);font-family:"Montserrat",sans-serif;position:relative}
  .card{position:absolute;left:82px;width:733px;height:428px;border-radius:22px;overflow:hidden;box-shadow:0 6px 18px rgba(0,0,0,.25)}
  .card--front{top:138px;background:var(--white)}
  .card--back{top:632px;background:var(--white)}
  .card-art{position:absolute;inset:0;width:100%;height:100%}

  .wordmark{position:absolute;display:flex;align-items:center;gap:14px;font-weight:800;text-transform:uppercase;line-height:1.08;white-space:nowrap}
  .wordmark__square{width:58px;height:58px;background:var(--red);flex:none}
  .wordmark__name{display:flex;flex-direction:column}
  .wordmark__line{display:block;letter-spacing:.4px}
  .wordmark__line--owner{font-size:18px}
  .wordmark__line--brand{font-size:26px}
  .wordmark__line--trade{font-size:17px;letter-spacing:1px}
  .card--front .wordmark{left:36px;top:44px;color:var(--ink)}
  .card--back .wordmark{left:50%;transform:translateX(-50%);top:30px;color:var(--white)}

  .contact{position:absolute;left:42px;top:302px}
  .contact__name{font-size:25px;font-weight:800;letter-spacing:.5px;color:var(--ink);margin-bottom:10px}
  .contact__name .first{color:var(--red)}
  .contact__row{display:flex;align-items:center;gap:10px;color:var(--ink)}
  .contact__row--phone{font-size:21px;font-weight:600;margin-bottom:8px}
  .contact__row--mail{font-size:15.5px;font-weight:500}
  .icon{flex:none}

  .tagline{position:absolute;top:172px;left:0;right:0;text-align:center;font-family:"Great Vibes",cursive;color:var(--white);font-size:27px;line-height:1}
  .supporters{position:absolute;top:246px;left:0;right:0;text-align:center;font-size:14px;font-weight:600;font-style:italic;color:var(--ink)}
  .badges{position:absolute;top:282px;left:0;right:0;display:flex;justify-content:center;align-items:center;gap:36px}
  .badge{display:block}
  .office{position:absolute;top:394px;left:0;right:0;display:flex;justify-content:center;align-items:center;gap:8px;color:var(--white);font-size:20px;font-weight:600}
  .office .label{color:var(--red)}
</style>
</head>
<body>

<section class="card card--front">
  <svg class="card-art" viewBox="0 0 733 428" preserveAspectRatio="none">
    <defs>
      <linearGradient id="roomTone" x1="0" y1="0" x2="1" y2="0">
        <stop offset="0" stop-color="var(--room-light)"/>
        <stop offset=".45" stop-color="var(--room-warm)"/>
        <stop offset=".78" stop-color="var(--room-glass)"/>
        <stop offset="1" stop-color="var(--room-plant)"/>
      </linearGradient>
      <linearGradient id="floorTone" x1="0" y1="0" x2="0" y2="1">
        <stop offset=".55" stop-color="var(--room-floor)" stop-opacity="0"/>
        <stop offset="1" stop-color="var(--room-floor)" stop-opacity=".8"/>
      </linearGradient>
    </defs>
    <g role="img" aria-label="Photo of a bright high-end living room with white sofas, blue cushions, a stone fireplace, tall windows and a palm plant">
      <rect width="733" height="428" fill="url(#roomTone)"/>
      <rect width="733" height="428" fill="url(#floorTone)"/>
    </g>
    <path d="M0 0 H520 C450 120 270 185 0 182 Z" fill="var(--white)"/>
    <path d="M0 182 C270 185 450 120 520 0 H530 C460 140 280 200 0 196 Z" fill="var(--red)"/>
    <path d="M0 246 C220 234 380 300 446 428 H0 Z" fill="var(--white)"/>
    <path d="M0 246 C220 234 380 300 446 428 H478 C404 286 240 222 0 236 Z" fill="var(--black)"/>
  </svg>

  <div class="wordmark">
    <span class="wordmark__square"></span>
    <span class="wordmark__name">
      <span class="wordmark__line wordmark__line--owner">Dale Whitcombe</span>
      <span class="wordmark__line wordmark__line--brand">Bramwick</span>
      <span class="wordmark__line wordmark__line--trade">Drywall Services</span>
    </span>
  </div>

  <div class="contact">
    <div class="contact__name"><span class="first">DALE</span> WHITCOMBE</div>
    <div class="contact__row contact__row--phone">
      <svg class="icon" width="14" height="20" viewBox="0 0 14 20"><rect x="1" y="1" width="12" height="18" rx="2" fill="none" stroke="var(--red)" stroke-width="2"/><circle cx="7" cy="15.5" r="1.2" fill="var(--red)"/></svg>
      (214) 555-0148
    </div>
    <div class="contact__row contact__row--mail">
      <svg class="icon" width="16" height="12" viewBox="0 0 16 12"><rect width="16" height="12" fill="var(--red)"/><path d="M0 0 L8 7 L16 0" fill="none" stroke="var(--white)" stroke-width="1.5"/></svg>
      Dale@BramwickDrywallServices.com
    </div>
  </div>
</section>

<section class="card card--back">
  <svg class="card-art" viewBox="0 0 733 428" preserveAspectRatio="none">
    <rect width="733" height="428" fill="var(--white)"/>
    <path d="M0 0 H733 V138 C500 118 240 118 0 150 Z" fill="var(--black)"/>
    <path d="M0 150 C240 118 500 118 733 138 V200 C500 230 240 240 0 232 Z" fill="var(--red)"/>
    <path d="M0 428 V376 C240 360 500 360 733 376 V428 Z" fill="var(--black)"/>
  </svg>

  <div class="wordmark">
    <span class="wordmark__square"></span>
    <span class="wordmark__name">
      <span class="wordmark__line wordmark__line--owner">Dale Whitcombe</span>
      <span class="wordmark__line wordmark__line--brand">Bramwick</span>
      <span class="wordmark__line wordmark__line--trade">Drywall Services</span>
    </span>
  </div>

  <p class="tagline">Specialising in Quality Residential &amp; Commercial Interiors<br>Since 1982</p>
  <p class="supporters">Proud Supporters</p>

  <div class="badges">
    <svg class="badge" width="204" height="60" viewBox="0 0 204 60" role="img" aria-label="Partner badge"><rect x="1" y="8" width="202" height="44" rx="6" fill="var(--badge-blue)" stroke="var(--badge-edge)"/></svg>
    <svg class="badge" width="96" height="78" viewBox="0 0 96 78" role="img" aria-label="Industry membership badge"><rect x="1" y="1" width="94" height="76" rx="6" fill="var(--badge-grey)" stroke="var(--badge-edge)"/></svg>
    <svg class="badge" width="242" height="60" viewBox="0 0 242 60" role="img" aria-label="Builders association badge"><rect x="1" y="8" width="240" height="44" rx="6" fill="var(--badge-teal)" stroke="var(--badge-edge)"/></svg>
  </div>

  <div class="office">
    <svg class="icon" width="19" height="19" viewBox="0 0 24 24"><path d="M6.6 10.8c1.4 2.8 3.8 5.2 6.6 6.6l2.2-2.2c.3-.3.7-.4 1-.2 1.1.4 2.3.6 3.6.6.6 0 1 .4 1 1V20c0 .6-.4 1-1 1C10.6 21 3 13.4 3 4c0-.6.4-1 1-1h3.5c.6 0 1 .4 1 1 0 1.3.2 2.5.6 3.6.1.3 0 .7-.2 1z" fill="var(--red)"/></svg>
    (817) 555-0192 <span class="label">(Office)</span>
  </div>
</section>

</body>
</html>
```